Packaging Tape Design for Retail / Ecommerce Company

We need a design for custom packing tape for our company. We would like to see two designs for the packaging tape. 1) with the word fragile attached 2) Similiar design without the fragileMinimum resolution is 300 .ppi 3" x 6" or 3" x 12" - If selected, request that font that are used be identified. ZOR Havenly Logo and package - Nest Bright! is a tagline we use on documents and correspondence. Looking for a creative design.

Target Market(s)

Mid level to high end consumers

Industry/Entity Type

Retail

Font styles to use
Sans Serif

Requirements
Must have
• logo must be included
• Nest Bright! - must be included
• web address: zorhavenly.example
Nice to have
• creativity

```html
<!DOCTYPE html>
<html lang="en">
<head>
<meta charset="utf-8">
<title>ZOR Havenly – Fragile Packing Tape</title>
<link rel="stylesheet" href="https://fonts.googleapis.com/css2?family=Russo+One&family=Saira+Stencil+One&display=swap">
<style>
  :root {
    --tape-white: #ffffff;
    --brand-red: #8c1c13;
    --olive: #7b7350;
    --tag-text: #ffffff;
  }
  html, body {
    margin: 0;
    padding: 0;
    overflow: hidden;
    background: var(--tape-white);
  }
  .tape {
    position: relative;
    width: 1200px;
    height: 300px;
    background: var(--tape-white);
    overflow: hidden;
  }
  .band {
    position: absolute;
    left: 0;
    width: 1200px;
    background: var(--brand-red);
  }
  .band--top-thick { top: 6px; height: 18px; }
  .band--top-thin { top: 31px; height: 5px; }
  .band--bottom-thin { top: 263px; height: 5px; }
  .band--bottom-thick { top: 275px; height: 19px; }

  .fragile-word {
    position: absolute;
    left: 0;
    top: 57px;
    margin: 0;
    font-family: "Saira Stencil One", "Arial Black", sans-serif;
    font-weight: 400;
    font-size: 176px;
    line-height: 1;
    letter-spacing: 1px;
    color: var(--olive);
    white-space: nowrap;
    transform: scaleX(0.82);
    transform-origin: left top;
  }

  .tagline-tag {
    position: absolute;
    left: 648px;
    top: 117px;
    width: 226px;
    height: 46px;
    border-radius: 12px;
    background: var(--brand-red);
    transform: rotate(20deg);
    display: flex;
    align-items: center;
    justify-content: center;
  }
  .tagline-tag span {
    font-family: "Russo One", sans-serif;
    font-size: 21px;
    letter-spacing: 1px;
    color: var(--tag-text);
    white-space: nowrap;
  }

  .brand-block {
    position: absolute;
    left: 945px;
    top: 95px;
    width: 250px;
    text-align: center;
    font-family: "Russo One", sans-serif;
    color: var(--brand-red);
  }
  .brand-name {
    margin: 0;
    font-size: 34px;
    line-height: 46px;
    white-space: nowrap;
  }
  .brand-web {
    margin: 14px 0 0;
    font-size: 15px;
    line-height: 20px;
    letter-spacing: 1px;
    white-space: nowrap;
  }
</style>
</head>
<body>
  <div class="tape">
    <div class="band band--top-thick"></div>
    <div class="band band--top-thin"></div>

    <h1 class="fragile-word">FRAGILE</h1>

    <div class="tagline-tag"><span>NEST BRIGHT!</span></div>

    <div class="brand-block">
      <p class="brand-name">ZOR Havenly</p>
      <p class="brand-web">zorhavenly.example</p>
    </div>

    <div class="band band--bottom-thin"></div>
    <div class="band band--bottom-thick"></div>
  </div>
</body>
</html>
```